Australian Meat, Seafood and Fresh Produce Website

Our organization is looking to design a simple, but eye catching website to show our services.
Our company exports West Australian FRESH fruit and vegetables, seafood and meat.
The website we are looking for would consist of:
- Landing Page
- Company info
- Directors bio
- Page that highlights our products
- Contact us page
We would like it to have a Chinese translated version as well.
Tobin
Target Market(s)
Chinese Market
Industry/Entity Type
It Company
Number of Pages Required
1 page
Look and feel
Each slider illustrates characteristics of the customer's brand and the style your logo design should communicate.

```html
<!DOCTYPE html>
<html lang="en">
<head>
<meta charset="utf-8">
<title>Westgate Fresh</title>
<link href="https://fonts.googleapis.com/css2?family=Open+Sans:wght@400;600;700&display=swap" rel="stylesheet">
<style>
:root{
  --green:#7dc242;
  --green-dark:#5a9a2a;
  --orange:#f47b20;
  --ink:#333;
  --muted:#666;
  --grey-band:#ececec;
  --footer:#1d3510;
  --footer-bottom:#0f1d08;
  --footer-text:#e4ecdc;
  --white:#fff;
}
*{margin:0;padding:0;box-sizing:border-box}
html,body{width:960px;height:1200px;overflow:hidden;background:var(--white)}
body{font-family:"Open Sans",sans-serif;color:var(--ink)}
.stage{position:absolute;left:0;top:0;width:1200px;height:1500px;transform:scale(.8);transform-origin:0 0}
.page{position:absolute;left:291px;top:0;width:618px;height:1500px}
.abs{position:absolute}
/* header */
.brand{left:41px;top:8px;display:flex;align-items:center;gap:6px}
.brand-dot{width:26px;height:26px;border-radius:50%;border:3px solid var(--green)}
.brand-name{font-size:18px;font-weight:700;color:var(--orange);line-height:1}
.phone{left:499px;top:12px;font-size:10px;display:flex;align-items:center;gap:5px;color:var(--ink)}
.nav{left:315px;top:33px;display:flex;gap:22px;font-size:8px;color:var(--green)}
/* hero */
.hero{left:0;top:56px;width:618px;height:259px;background:linear-gradient(90deg,#b9aa92 0%,#c9bca6 45%,#8f6d4a 60%,#5f8b3a 80%,#3f6e22 100%)}
.hero-title{left:42px;top:138px;color:var(--white);font-size:23px;line-height:30px;font-weight:400;white-space:nowrap}
.hero-title span{display:inline-block;background:rgba(70,60,48,.82);padding:0 9px}
.hero-title span + br + span{padding-bottom:6px}
.hero-sub{left:41px;top:211px;font-size:10.5px;color:#3a2f25;line-height:14px}
.dots{left:42px;top:247px;display:flex;gap:5px}
.dots span{width:4px;height:4px;border-radius:50%;background:#5b4d3d}
/* band */
.band{left:0;top:315px;width:618px;height:92px;background:var(--green)}
.band-text{left:0;top:324px;width:618px;text-align:center;color:var(--white);font-size:11.5px;line-height:16px;letter-spacing:.3px}
.cat{width:124px;height:84px;border:3px solid var(--white);top:362px;overflow:hidden}
.cat .ph{width:100%;height:100%}
.cat b{position:absolute;left:4px;bottom:0;font-size:19px;color:var(--white);font-weight:700}
/* welcome */
.welcome-title{left:41px;top:468px;font-size:13.5px;font-weight:400;color:var(--orange);width:304px;border-bottom:1px solid var(--green);padding-bottom:5px}
.welcome-copy{left:41px;top:503px;width:290px;font-size:6.5px;line-height:11px;color:var(--muted)}
.ticks{left:365px;top:504px;font-size:6.5px;color:var(--orange);list-style:none}
.ticks li{height:14px;display:flex;align-items:center;gap:4px}
/* steps */
.steps{left:0;top:584px;width:618px;height:160px;background:var(--grey-band)}
.steps-photo{left:0;top:584px;width:210px;height:160px;background:linear-gradient(120deg,#d9a57c,#c9c4b8 55%,#ececec)}
.step-label{font-size:10.5px;color:#222;width:80px;text-align:center;top:702px}
/* services */
.svc-img{top:777px;width:124px;height:84px;border:3px solid var(--orange)}
.svc-title{top:872px;width:124px;text-align:center;font-size:11px;color:var(--green)}
.svc-rule{top:887px;width:116px;height:1px;background:#cfe3bd}
.svc-copy{top:896px;width:124px;text-align:center;font-size:6.3px;line-height:11px;color:var(--muted)}
.btn{width:52px;height:14px;background:var(--orange);color:var(--white);font-size:6px;text-align:center;line-height:14px}
/* testimonial */
.testi{left:0;top:979px;width:618px;height:158px;background:linear-gradient(90deg,#6fa83a 0%,#7cb545 55%,#8aa54d 70%,#b55a3e 85%,#c46b56 100%)}
.testi-title{left:42px;top:1002px;font-size:13px;color:#b43a12;display:flex;gap:10px;align-items:center}
.testi-quote{left:68px;top:1038px;width:372px;font-size:6.5px;line-height:11px;color:var(--white)}
.qmark{font-size:40px;font-weight:700;color:#2e4a17;line-height:1}
.testi-name{left:68px;top:1093px;font-size:7px;font-weight:700;color:#1e2e10}
.testi-role{left:75px;top:1103px;font-size:5.5px;color:#1e2e10}
/* directors */
.face{top:1162px;width:91px;height:91px;border-radius:50%;border:3px solid var(--orange);background:linear-gradient(#9a9a9a,#555)}
.dname{top:1259px;width:134px;text-align:center;font-size:11px;color:var(--green)}
.drole{top:1283px;width:134px;text-align:center;font-size:6.3px;line-height:11px;color:var(--muted)}
.drole b{color:#222}
/* footer */
.footer{left:0;top:1371px;width:618px;height:110px;background:var(--footer)}
.footer-bottom{left:0;top:1481px;width:618px;height:19px;background:var(--footer-bottom);color:#9aa590;font-size:5.5px;text-align:center;line-height:19px}
.fcol{top:1384px;font-size:6.3px;line-height:11px;color:var(--footer-text)}
.fcol h4{font-size:7.5px;font-weight:700;color:var(--white);border-bottom:1px solid #4d6a37;padding-bottom:3px;margin-bottom:6px}
.fcol ul{list-style:none}
.fcol li::before{content:"▸ ";font-size:5px}
.social{display:flex;align-items:center;gap:6px;height:17.5px}
.social i{width:12px;height:12px;background:#3b7dc4;display:block}
.news-note{font-size:5.3px;line-height:8px}
.news-input{width:104px;height:12px;background:var(--white);color:#999;font-size:5px;padding-left:4px;line-height:12px;margin-top:4px}
.news-btn{width:38px;height:11px;background:var(--orange);color:var(--white);font-size:5px;text-align:center;line-height:11px;margin-top:5px;font-weight:700}
</style>
</head>
<body>
<div class="stage">
<div class="page">

  <header>
    <div class="abs brand"><span class="brand-dot"></span><span class="brand-name">WESTGATE FRESH</span></div>
    <div class="abs phone">
      <svg width="13" height="13" viewBox="0 0 24 24"><circle cx="12" cy="12" r="11" fill="none" stroke="#333" stroke-width="2"/><path d="M8 6l2 3-1.5 1.5a8 8 0 0 0 5 5L15 14l3 2-1 2c-5 0-10-5-10-10z" fill="#333"/></svg>
      555 018 2240
    </div>
    <nav class="abs nav"><span>HOME</span><span>ABOUT</span><span>PRODUCTS</span><span>DIRECTORS</span><span>CONTACT</span></nav>
  </header>

  <section>
    <div class="abs hero" role="img" aria-label="Fresh tomatoes, apples, onion and greens on a wooden table"></div>
    <h1 class="abs hero-title"><span>WE ARE A LEADING</span><br><span>FRESH FOOD COMPANY</span></h1>
    <p class="abs hero-sub">FRESH FOOD FOR FRESH EATING.<br>HAVE IT YOUR WAY.</p>
    <div class="abs dots"><span></span><span></span><span></span><span></span></div>
  </section>

  <section>
    <div class="abs band"></div>
    <svg class="abs" style="left:0;top:401px" width="618" height="8"><path d="M0 0 Q3 8 6 0 Q9 8 12 0 Q15 8 18 0 Q21 8 24 0 Q27 8 30 0 Q33 8 36 0Z" fill="#7dc242"/><path d="M582 0 Q585 8 588 0 Q591 8 594 0 Q597 8 600 0 Q603 8 606 0 Q609 8 612 0 Q615 8 618 0Z" fill="#7dc242"/></svg>
    <p class="abs band-text">WESTGATE FRESH (WGF) AIMS TO SUPPLY HIGH QUALITY WEST AUSTRALIAN PRODUCE<br>TO THE REST OF THE WORLD</p>
    <div class="abs cat" style="left:41px"><div class="ph" role="img" aria-label="Cuts of raw meat" style="background:linear-gradient(135deg,#c9474a,#e3a6a0)"></div><b>MEAT</b></div>
    <div class="abs cat" style="left:178px"><div class="ph" role="img" aria-label="Seafood platter" style="background:linear-gradient(135deg,#c98c6a,#8a9aa6)"></div><b>SEAFOOD</b></div>
    <div class="abs cat" style="left:316px"><div class="ph" role="img" aria-label="Assorted fresh fruit" style="background:linear-gradient(135deg,#e7b12a,#d6452e 60%,#6fa83a)"></div><b>FRUIT</b></div>
    <div class="abs cat" style="left:453px"><div class="ph" role="img" aria-label="Assorted fresh vegetables" style="background:linear-gradient(135deg,#5a8a2e,#b53a3a 60%,#e38b2a)"></div><b>VEGETABLE</b></div>
  </section>

  <section>
    <h2 class="abs welcome-title">WELCOME TO WESTGATE FRESH</h2>
    <p class="abs welcome-copy">Western Australia is known for its high quality farming practices and environment, which produces meat, seafood, fruit and vegetable of a caliber that is respected globally. With a management team and first class suppliers allows our organization to provide quality ingredients, straight from farm or ocean to purchaser, in a timely manner to the highest quality.</p>
    <ul class="abs ticks">
      <li><svg width="8" height="8" viewBox="0 0 10 10"><path d="M1 5l3 3 5-7" stroke="#7dc242" stroke-width="2" fill="none"/></svg>We are Australia's leading independent Food Service Distributor</li>
      <li><svg width="8" height="8" viewBox="0 0 10 10"><path d="M1 5l3 3 5-7" stroke="#7dc242" stroke-width="2" fill="none"/></svg>We take pride in our business and the exceptional service we offer!</li>
      <li><svg width="8" height="8" viewBox="0 0 10 10"><path d="M1 5l3 3 5-7" stroke="#7dc242" stroke-width="2" fill="none"/></svg>We are dedicated and committed to our service</li>
    </ul>
  </section>

  <section>
    <div class="abs steps"></div>
    <div class="abs steps-photo" role="img" aria-label="Whole fish, prawns and bay leaves scattered with peppercorns"></div>
    <svg class="abs" style="left:300px;top:610px" width="290" height="90">
      <g fill="none" stroke="#7dc242" stroke-width="2">
        <circle cx="32" cy="20" r="16"/><circle cx="147" cy="20" r="16"/><circle cx="260" cy="20" r="16"/>
      </g>
      <g fill="#7dc242" font-family="Open Sans,sans-serif" font-size="19" text-anchor="middle">
        <text x="32" y="27">1</text><text x="147" y="27">2</text><text x="260" y="27">3</text>
      </g>
      <g stroke="#f47b20" stroke-width="2" stroke-dasharray="2 4" fill="none"><path d="M57 20h58"/><path d="M171 20h58"/></g>
      <path d="M114 16l6 4-6 4M228 16l6 4-6 4" stroke="#f47b20" stroke-width="1.5" fill="none"/>
      <g fill="#3f6e22">
        <circle cx="24" cy="78" r="7"/><circle cx="35" cy="76" r="8"/><circle cx="44" cy="79" r="6"/>
        <path d="M122 58h6l5 16h16l3-10h-20" fill="none" stroke="#3f6e22" stroke-width="3"/>
        <circle cx="135" cy="82" r="3"/><circle cx="148" cy="82" r="3"/>
        <rect x="224" y="58" width="26" height="20"/><path d="M252 64h8l6 7v7h-14z"/>
        <circle cx="232" cy="81" r="4" stroke="#ececec" stroke-width="2"/><circle cx="259" cy="81" r="4" stroke="#ececec" stroke-width="2"/>
      </g>
    </svg>
    <div class="abs step-label" style="left:292px">BROWSE</div>
    <div class="abs step-label" style="left:405px">ORDER</div>
    <div class="abs step-label" style="left:514px">ENJOY</div>
  </section>

  <section>
    <div class="abs svc-img" style="left:41px;background:linear-gradient(135deg,#8d8d8d,#c7c0b0)" role="img" aria-label="Shopper choosing produce in a wholesale market"></div>
    <div class="abs svc-img" style="left:178px;background:linear-gradient(135deg,#e6e6e6,#9a9a8a)" role="img" aria-label="Chef plating a dish"></div>
    <div class="abs svc-img" style="left:316px;background:linear-gradient(135deg,#d5692f,#c7a44a 50%,#8a6d5c)" role="img" aria-label="Family shopping in a grocery store"></div>
    <div class="abs svc-img" style="left:453px;background:linear-gradient(135deg,#5c5c66,#9b8a5a 60%,#6a7a4a)" role="img" aria-label="Supermarket produce aisle"></div>

    <div class="abs svc-title" style="left:41px">WHOLESALE</div>
    <div class="abs svc-title" style="left:178px">FOOD SERVICE</div>
    <div class="abs svc-title" style="left:316px">RETAIL</div>
    <div class="abs svc-title" style="left:453px">EXPORT</div>
    <div class="abs svc-rule" style="left:45px"></div>
    <div class="abs svc-rule" style="left:182px"></div>
    <div class="abs svc-rule" style="left:320px"></div>
    <div class="abs svc-rule" style="left:457px"></div>

    <p class="abs svc-copy" style="left:41px">It is a long established fact that a reader will be distracted by the readable content of a page when looking at its layout.</p>
    <p class="abs svc-copy" style="left:178px">It is a long established fact that a reader will be distracted by the readable content of a page when looking at its layout.</p>
    <p class="abs svc-copy" style="left:316px">It is a long established fact that a reader will be distracted by the readable content of a page when looking at its layout.</p>
    <p class="abs svc-copy" style="left:453px">It is a long established fact that a reader will be distracted by the readable content of a page when looking at its layout.</p>

    <div class="abs btn" style="left:77px;top:941px">READ MORE</div>
    <div class="abs btn" style="left:215px;top:941px">READ MORE</div>
    <div class="abs btn" style="left:352px;top:941px">READ MORE</div>
    <div class="abs btn" style="left:489px;top:941px">READ MORE</div>
  </section>

  <section>
    <div class="abs testi" role="img" aria-label="Green wooden backdrop with tomatoes, mushrooms and raw meat on a board"></div>
    <div class="abs testi-title">TESTIMONIAL <svg width="20" height="10"><path d="M5 1L1 5l4 4M15 1l4 4-4 4" stroke="#fff" fill="none" stroke-width="1.2"/></svg></div>
    <div class="abs qmark" style="left:40px;top:1028px">“</div>
    <p class="abs testi-quote">It is a long established fact that a reader will be distracted by the readable content of a page when looking at its layout. The point of using Lorem Ipsum is that it has a more-or-less normal distribution of letters, as opposed to here, making it look like readable English. Many desktop publishing packages and web page editors Lorem Ipsum is that it has a more-or-less normal distribution of letters, as opposed.</p>
    <div class="abs qmark" style="left:243px;top:1066px">”</div>
    <div class="abs testi-name">Daniel Reeve</div>
    <div class="abs testi-role">Customer</div>
  </section>

  <section>
    <div class="abs face" style="left:57px" role="img" aria-label="Portrait of Jared Tobin"></div>
    <div class="abs face" style="left:195px" role="img" aria-label="Portrait of Marcus Hale"></div>
    <div class="abs face" style="left:332px" role="img" aria-label="Portrait of Owen Carraway"></div>
    <div class="abs face" style="left:470px" role="img" aria-label="Portrait of Dr Mei Ruan"></div>

    <div class="abs dname" style="left:36px">JARED TOBIN</div>
    <div class="abs dname" style="left:174px">MARCUS HALE</div>
    <div class="abs dname" style="left:311px">OWEN CARRAWAY</div>
    <div class="abs dname" style="left:449px">DR MEI RUAN</div>

    <p class="abs drole" style="left:36px"><b>Role:</b> Management of operations, Chinese liaison, Quality processes and management.</p>
    <p class="abs drole" style="left:174px"><b>Role:</b> Procurement and liaison with suppliers.</p>
    <p class="abs drole" style="left:311px"><b>Role:</b> Logistics, transport, customs and tariffs.</p>
    <p class="abs drole" style="left:449px"><b>Role:</b> Chinese Market Specialist, liaison between Australia and Chinese activities.</p>

    <div class="abs btn" style="left:77px;top:1329px">READ MORE</div>
    <div class="abs btn" style="left:215px;top:1329px">READ MORE</div>
    <div class="abs btn" style="left:352px;top:1329px">READ MORE</div>
    <div class="abs btn" style="left:489px;top:1329px">READ MORE</div>
  </section>

  <footer>
    <div class="abs footer"></div>
    <div class="abs fcol" style="left:41px;width:88px">
      <h4>QUICK LINKS</h4>
      <ul><li>HOME</li><li>ABOUT</li><li>PRODUCTS</li><li>DIRECTORS</li><li>CONTACT</li></ul>
    </div>
    <div class="abs fcol" style="left:156px;width:146px">
      <h4>CONTACT INFORMATION</h4>
      <p style="padding-left:11px;line-height:9px">14 Harbour Row 6160 Fremantle,<br>Australia</p>
      <p style="padding-left:11px;margin-top:5px">+61 (08) 5550 1742</p>
      <p style="padding-left:11px;margin-top:4px">hello@westgatefresh.example</p>
    </div>
    <svg class="abs" style="left:156px;top:1403px" width="8" height="52"><path d="M4 0a3 3 0 0 1 3 3c0 2-3 5-3 5S1 5 1 3a3 3 0 0 1 3-3z" fill="#e4ecdc"/><path d="M2 24q0 5 4 6l1-1-1-2-1 1q-1-2-1-4l1 0 0-2-2 0z" fill="#e4ecdc"/><rect x="0" y="39" width="7" height="5" fill="#e4ecdc"/></svg>
    <div class="abs fcol" style="left:329px;width:125px">
      <h4>NEWSLETTER SIGNUP</h4>
      <p class="news-note">Please enter your email address below to receive our FREE newsletter</p>
      <div class="news-input">Your Email ID</div>
      <div class="news-btn">SUBSCRIBE</div>
    </div>
    <div class="abs fcol" style="left:480px;width:97px">
      <h4>FOLLOW US</h4>
      <div class="social"><i></i>Newsfeed</div>
      <div class="social"><i style="background:#d9a21b"></i>Network</div>
      <div class="social"><i style="background:#2ba6dc"></i>Updates</div>
      <div class="social"><i style="background:#6aa8d8"></i>Email</div>
    </div>
    <div class="abs footer-bottom">Copyright© 2015 westgatefresh.example</div>
  </footer>

</div>
</div>
</body>
</html>
```